Business Card Design for new logo

Business card Design for new logo. Follow colors from logo.
The company has offices in multiple comtries
Want to have some bulltes on the countries and also on the main services

Something like
USA*Dominican Republic*LATAM

Consulting*Healthcare IT*Tranformation

Industry/Entity Type

Information Technology

Contact Information for Business Card

Address, Phones, countries, name and position

Lucan morrel

Founder and CEO

947 Tarrow Ln
Harlow Ridge, PA 17588

Lmorrel@quendoxcare.com

www.quendoxcare.com

555-304-6182

555-222-2222

```html
<!DOCTYPE html>
<html lang="en">
<head>
<meta charset="utf-8">
<title>Quendox Care – Business Cards</title>
<link href="https://fonts.googleapis.com/css2?family=Philosopher:wght@700&family=Roboto:wght@400;500&display=swap" rel="stylesheet">
<style>
  :root {
    --stage: #333333;
    --brand-blue: #0a78b5;
    --brand-orange: #e8864a;
    --label-red: #ff0000;
    --ink: #333333;
    --white: #ffffff;
  }
  * { margin: 0; padding: 0; box-sizing: border-box; }
  html, body { width: 1200px; height: 789px; overflow: hidden; background: var(--stage); }
  .canvas { position: relative; width: 1200px; height: 789px; font-family: "Roboto", Arial, sans-serif; }
  .lang-label { position: absolute; top: 76px; width: 462px; text-align: center; color: var(--label-red); font-size: 43px; font-weight: 400; }
  .card { position: absolute; width: 462px; height: 271px; overflow: hidden; }
  .card-front { top: 151px; background: var(--brand-blue); color: var(--white); text-align: center; }
  .card-back { top: 434px; background: var(--white); color: var(--ink); }
  .col-en { left: 120px; }
  .col-es { left: 617px; }

  .front-name { position: absolute; left: 0; right: 0; top: 90px; font-family: "Philosopher", Georgia, serif; font-weight: 700; font-size: 46px; line-height: 1; }
  .front-services { position: absolute; left: 0; right: 0; top: 145px; font-size: 14px; }
  .front-regions { position: absolute; left: 0; right: 0; top: 233px; font-size: 12px; }
  .sep { margin: 0 6px; }
  .chev { margin: 0 9px; font-size: 10px; }

  .accent-arc { position: absolute; left: -58px; top: 18px; width: 76px; height: 76px; border-radius: 50%; background: var(--brand-orange); }
  .person-name { position: absolute; left: 31px; top: 38px; font-family: "Philosopher", Georgia, serif; font-weight: 700; font-size: 19px; color: var(--brand-blue); }
  .person-role { position: absolute; left: 31px; top: 62px; font-size: 12px; }
  .brand-name { position: absolute; right: 28px; top: 98px; font-family: "Philosopher", Georgia, serif; font-weight: 700; font-size: 33px; color: var(--brand-blue); line-height: 1; }
  .contact-list { position: absolute; left: 34px; top: 170px; list-style: none; font-size: 12.5px; }
  .contact-list li { display: flex; align-items: center; height: 17.5px; }
  .contact-list svg { width: 11px; height: 11px; margin-right: 11px; fill: var(--brand-orange); }
  .address { position: absolute; right: 28px; top: 184px; text-align: right; font-size: 12.5px; line-height: 17.5px; }
  .bands { position: absolute; left: 0; bottom: 0; width: 462px; height: 41px; }
  .band-services { position: absolute; right: 0; bottom: 12px; width: 270px; text-align: center; color: var(--white); font-size: 11.5px; }
  .band-services.compact { font-size: 10.5px; letter-spacing: -0.1px; }
</style>
</head>
<body>
<div class="canvas">
  <div class="lang-label" style="left:120px">English</div>
  <div class="lang-label" style="left:617px">Spanish</div>

  <!-- English front -->
  <section class="card card-front col-en">
    <div class="front-name">Quendox Care</div>
    <div class="front-services">Consulting<span class="sep">|</span>Healthcare IT<span class="sep">|</span>Transformation</div>
    <div class="front-regions"><span class="chev">»</span>USA<span class="chev">»</span>Dominican Republic<span class="chev">»</span>LATAM</div>
  </section>

  <!-- Spanish front -->
  <section class="card card-front col-es">
    <div class="front-name">Quendox Care</div>
    <div class="front-services">Consultoría<span class="sep">|</span>Tecnología en salud<span class="sep">|</span>Transformación</div>
    <div class="front-regions"><span class="chev">»</span>USA<span class="chev">»</span>Republica Dominicana<span class="chev">»</span>America Latina</div>
  </section>

  <!-- English back -->
  <section class="card card-back col-en">
    <div class="accent-arc"></div>
    <div class="person-name">Lucan Morrel</div>
    <div class="person-role">Founder &amp; CEO</div>
    <div class="brand-name">Quendox Care</div>
    <ul class="contact-list">
      <li><svg viewBox="0 0 12 12"><path d="M3 0h6a1 1 0 0 1 1 1v10a1 1 0 0 1-1 1H3a1 1 0 0 1-1-1V1a1 1 0 0 1 1-1zm0 2v7h6V2z"/></svg>555-304-6182</li>
      <li><svg viewBox="0 0 12 12"><path d="M0 4c2-3 10-3 12 0l-2 1.5-1.5-1.5v-1h-5v1L2 5.5zM2 7h8l1 4H1z"/></svg>555-222-2222</li>
      <li><svg viewBox="0 0 12 12"><path d="M0 2h12v8H0zm1 1 5 4 5-4z"/></svg>Lmorrel@quendoxcare.com</li>
      <li><svg viewBox="0 0 12 12"><circle cx="6" cy="6" r="5.5"/></svg>www.quendoxcare.com</li>
    </ul>
    <div class="address">947 Tarrow Ln<br>Harlow Ridge, PA 17588</div>
    <svg class="bands" viewBox="0 0 462 41" aria-hidden="true">
      <rect x="0" y="27" width="190" height="14" fill="var(--brand-orange)"/>
      <polygon points="200,0 462,0 462,41 178,41" fill="var(--brand-blue)"/>
    </svg>
    <div class="band-services">Consulting<span class="sep">|</span>Healthcare IT<span class="sep">|</span>Transformation</div>
  </section>

  <!-- Spanish back -->
  <section class="card card-back col-es">
    <div class="accent-arc"></div>
    <div class="person-name">Lucan Morrel</div>
    <div class="person-role">Presidente &amp; Socio Fundador</div>
    <div class="brand-name">Quendox Care</div>
    <ul class="contact-list">
      <li><svg viewBox="0 0 12 12"><path d="M3 0h6a1 1 0 0 1 1 1v10a1 1 0 0 1-1 1H3a1 1 0 0 1-1-1V1a1 1 0 0 1 1-1zm0 2v7h6V2z"/></svg>555-304-6182</li>
      <li><svg viewBox="0 0 12 12"><path d="M0 4c2-3 10-3 12 0l-2 1.5-1.5-1.5v-1h-5v1L2 5.5zM2 7h8l1 4H1z"/></svg>555-222-2222</li>
      <li><svg viewBox="0 0 12 12"><path d="M0 2h12v8H0zm1 1 5 4 5-4z"/></svg>Lmorrel@quendoxcare.com</li>
      <li><svg viewBox="0 0 12 12"><circle cx="6" cy="6" r="5.5"/></svg>www.quendoxcare.com</li>
    </ul>
    <div class="address">947 Tarrow Ln<br>Harlow Ridge, PA 17588</div>
    <svg class="bands" viewBox="0 0 462 41" aria-hidden="true">
      <rect x="0" y="27" width="190" height="14" fill="var(--brand-orange)"/>
      <polygon points="200,0 462,0 462,41 178,41" fill="var(--brand-blue)"/>
    </svg>
    <div class="band-services compact">Consultoría | Tecnología en salud | Transformación</div>
  </section>
</div>
</body>
</html>
```